Corrindale Planners, LLC Stationary

Corrindale Planners, LLC is a new financial planning and consulting company. We are looking for designs on business cards, letterhead, envelopes, and anything else that would be useful. Our preference for business card design is two sided. We are looking for a professional and clean look with incorporating the logo and patriotic feel. Thank you to all who participate and good luck!

```html
<!DOCTYPE html>
<html lang="en">
<head>
<meta charset="utf-8">
<title>Corrindale Planners, LLC – Stationery</title>
<link href="https://fonts.googleapis.com/css2?family=Open+Sans:wght@400;600;700&display=swap" rel="stylesheet">
<style>
:root{
  --navy:#0f3e6a;
  --red:#c8202c;
  --backdrop:#b4b4b4;
  --paper:#ffffff;
  --mark-soft:#e6e9ee;
  --mark-blush:#f6e1e3;
}
*{box-sizing:border-box;margin:0;padding:0}
html,body{width:1200px;height:960px;overflow:hidden}
body{background:var(--backdrop);font-family:'Open Sans',Arial,sans-serif;color:var(--navy);position:relative}
.piece{position:absolute;background:var(--paper);box-shadow:10px 12px 14px rgba(0,0,0,.45);overflow:hidden}

/* name lockup */
.lockup{position:absolute;display:flex;align-items:center;gap:6px}
.lockup-dot{border-radius:50%;background:var(--red);flex:none}
.lockup-text{display:flex;flex-direction:column;line-height:1}
.lockup-name{font-weight:600;color:var(--navy);white-space:nowrap}
.lockup-tag{color:var(--navy);text-transform:uppercase;letter-spacing:.12em;margin-top:3px;white-space:nowrap}

.lockup.sm .lockup-dot{width:12px;height:12px}
.lockup.sm .lockup-name{font-size:10.5px}
.lockup.sm .lockup-tag{font-size:3.6px}
.lockup.md .lockup-dot{width:16px;height:16px}
.lockup.md .lockup-name{font-size:13px}
.lockup.md .lockup-tag{font-size:4.4px}
.lockup.lg .lockup-dot{width:26px;height:26px}
.lockup.lg .lockup-name{font-size:17px}
.lockup.lg .lockup-tag{font-size:6px}

.emblem-field{position:absolute;border-radius:50%;background:radial-gradient(circle at 60% 45%,var(--mark-blush),var(--mark-soft) 70%)}

/* cards */
.card{width:275px;height:158px}
.card-stripe{position:absolute;left:0;bottom:0;width:275px;height:11px}
.person{position:absolute;font-size:9px}
.person-name{font-weight:700;font-size:10px}
.contact-list{position:absolute;list-style:none;font-size:8px;line-height:12.3px;color:#1a1a1a}
.contact-list li{display:flex;align-items:center;gap:6px}
.contact-list svg{width:7px;height:7px;flex:none}
.address{position:absolute;font-size:8.4px;line-height:10px;color:var(--navy)}

.card-art{position:absolute;left:0;top:30px;width:120px;height:128px;background:linear-gradient(135deg,var(--navy) 0%,var(--navy) 45%,var(--red) 55%,var(--red) 100%);clip-path:polygon(0 20%,55% 0,100% 45%,70% 100%,0 100%)}

/* letterhead footer */
.footer-line{position:absolute;left:54px;bottom:18px;display:flex;gap:20px;align-items:center;font-size:5.6px;color:#1a1a1a}
.footer-line span{display:flex;align-items:center;gap:4px}
.footer-line svg{width:5px;height:5px}
.footer-line .footer-addr{color:var(--navy);border-left:1px solid var(--navy);padding-left:9px}

.slip-title{position:absolute;right:16px;top:11px;font-size:11.5px;color:var(--navy)}
.return-addr{position:absolute;left:15px;top:48px;font-size:5.4px;line-height:7px;color:var(--navy)}
.flap{position:absolute;left:0;top:0;width:467px;height:72px}
</style>
</head>
<body>

<!-- Letterhead -->
<section class="piece letterhead" style="left:54px;top:54px;width:455px;height:588px">
  <div class="lockup sm" style="left:156px;top:42px">
    <span class="lockup-dot"></span>
    <div class="lockup-text"><span class="lockup-name">Corrindale Planners, LLC</span><span class="lockup-tag">Financial planning and consulting</span></div>
  </div>
  <div class="emblem-field" role="img" aria-label="Faint brand emblem decoration" style="left:230px;top:370px;width:210px;height:210px"></div>
  <div class="footer-line">
    <span><svg viewBox="0 0 10 10"><path d="M2 1l2 0 1 3-1.5 1a6 6 0 0 0 2.5 2.5L7 6l3 1v2c-5 1-9-3-8-8z" fill="var(--red)"/></svg>+1 555 017 3381</span>
    <span><svg viewBox="0 0 10 10"><rect x="0" y="2" width="10" height="7" fill="var(--red)"/></svg>info@corrindaleplanners.com</span>
    <span><svg viewBox="0 0 10 10"><circle cx="5" cy="5" r="4.2" fill="none" stroke="var(--red)" stroke-width="1.4"/></svg>www.corrindaleplanners.com</span>
    <span class="footer-addr">480 Harlow Ave, Suite 210, Brookfield, CA 91420</span>
  </div>
</section>

<!-- Business card front, version 1 -->
<section class="piece card" style="left:554px;top:54px">
  <div class="person" style="left:17px;top:19px"><div class="person-name">Martin Hale</div>Director</div>
  <div class="lockup sm" style="left:142px;top:20px">
    <span class="lockup-dot"></span>
    <div class="lockup-text"><span class="lockup-name" style="font-size:8.4px">Corrindale Planners, LLC</span><span class="lockup-tag" style="font-size:3px">Financial planning and consulting</span></div>
  </div>
  <ul class="contact-list" style="left:17px;top:62px">
    <li><svg viewBox="0 0 10 10"><rect x="2.5" y="0.5" width="5" height="9" rx="1" fill="none" stroke="var(--red)" stroke-width="1.2"/></svg>+1 555 014 2290</li>
    <li><svg viewBox="0 0 10 10"><path d="M2 1l2 0 1 3-1.5 1a6 6 0 0 0 2.5 2.5L7 6l3 1v2c-5 1-9-3-8-8z" fill="var(--red)"/></svg>+1 555 017 3381</li>
    <li><svg viewBox="0 0 10 10"><rect x="0" y="2" width="10" height="7" fill="var(--red)"/></svg>info@corrindaleplanners.com</li>
    <li><svg viewBox="0 0 10 10"><circle cx="5" cy="5" r="4.2" fill="none" stroke="var(--red)" stroke-width="1.4"/></svg>www.corrindaleplanners.com</li>
  </ul>
  <div class="address" style="left:17px;top:120px">480 Harlow Ave, Suite 210<br>Brookfield, CA 91420</div>
  <svg class="card-stripe" viewBox="0 0 275 11" preserveAspectRatio="none"><polygon points="0,0 189,0 184,11 0,11" fill="var(--navy)"/><polygon points="194,0 275,0 275,11 189,11" fill="var(--red)"/></svg>
</section>

<!-- Business card back, version 1 -->
<section class="piece card" style="left:866px;top:54px">
  <div class="lockup lg" style="left:38px;top:66px">
    <span class="lockup-dot"></span>
    <div class="lockup-text"><span class="lockup-name">Corrindale Planners, LLC</span><span class="lockup-tag">Financial planning and consulting</span></div>
  </div>
  <svg class="card-stripe" viewBox="0 0 275 11" preserveAspectRatio="none"><polygon points="0,0 189,0 184,11 0,11" fill="var(--navy)"/><polygon points="194,0 275,0 275,11 189,11" fill="var(--red)"/></svg>
</section>

<!-- Business card front, version 2 -->
<section class="piece card" style="left:554px;top:235px">
  <div class="card-art" role="img" aria-label="Large brand emblem in navy and red"></div>
  <div class="person" style="left:145px;top:18px"><div class="person-name">Martin Hale</div>Director</div>
  <ul class="contact-list" style="left:145px;top:63px">
    <li><svg viewBox="0 0 10 10"><rect x="2.5" y="0.5" width="5" height="9" rx="1" fill="none" stroke="var(--red)" stroke-width="1.2"/></svg>+1 555 014 2290</li>
    <li><svg viewBox="0 0 10 10"><path d="M2 1l2 0 1 3-1.5 1a6 6 0 0 0 2.5 2.5L7 6l3 1v2c-5 1-9-3-8-8z" fill="var(--red)"/></svg>+1 555 017 3381</li>
    <li><svg viewBox="0 0 10 10"><rect x="0" y="2" width="10" height="7" fill="var(--red)"/></svg>info@corrindaleplanners.com</li>
    <li><svg viewBox="0 0 10 10"><circle cx="5" cy="5" r="4.2" fill="none" stroke="var(--red)" stroke-width="1.4"/></svg>www.corrindaleplanners.com</li>
  </ul>
  <div class="address" style="left:145px;top:121px">480 Harlow Ave, Suite 210<br>Brookfield, CA 91420</div>
</section>

<!-- Business card back, version 2 -->
<section class="piece card" style="left:866px;top:235px">
  <div class="lockup lg" style="left:38px;top:64px">
    <span class="lockup-dot"></span>
    <div class="lockup-text"><span class="lockup-name">Corrindale Planners, LLC</span><span class="lockup-tag">Financial planning and consulting</span></div>
  </div>
</section>

<!-- Compliments slip -->
<section class="piece slip" style="left:554px;top:445px;width:422px;height:198px">
  <div class="slip-title">With Compliments</div>
  <div class="emblem-field" role="img" aria-label="Faint brand emblem decoration" style="left:258px;top:45px;width:155px;height:155px"></div>
  <div class="lockup sm" style="left:19px;top:163px">
    <span class="lockup-dot"></span>
    <div class="lockup-text"><span class="lockup-name" style="font-size:9px">Corrindale Planners, LLC</span><span class="lockup-tag" style="font-size:3px">Financial planning and consulting</span></div>
  </div>
</section>

<!-- Envelope front -->
<section class="piece envelope" style="left:54px;top:689px;width:467px;height:234px">
  <div class="lockup sm" style="left:17px;top:22px">
    <span class="lockup-dot" style="width:11px;height:11px"></span>
    <div class="lockup-text"><span class="lockup-name" style="font-size:8.6px">Corrindale Planners, LLC</span><span class="lockup-tag" style="font-size:3px">Financial planning and consulting</span></div>
  </div>
  <div class="return-addr">480 Harlow Ave, Suite 210<br>Brookfield, CA 91420</div>
  <div class="emblem-field" role="img" aria-label="Faint brand emblem decoration" style="left:290px;top:75px;width:175px;height:175px"></div>
</section>

<!-- Envelope back -->
<section class="piece envelope-back" style="left:570px;top:689px;width:467px;height:234px">
  <svg class="flap" viewBox="0 0 467 72" preserveAspectRatio="none"><path d="M0 0H467L462 62Q461 70 452 70H15Q6 70 5 62Z" fill="var(--navy)"/></svg>
  <span style="position:absolute;left:222px;top:24px;width:22px;height:22px;border-radius:50%;background:var(--paper)"></span>
</section>

</body>
</html>
```